Benefit Porter

Need home page design for new website. The winner will have the opportunity to design the entire site.

I have attached 3 files.

1) Sort of a site map. PLEASE do not design the home page based on this wire frame. Be creative and use your expertise.

2) Tagline and Copy for the home page. Please just greek in or make up copy for areas that do not have copy at this time.

3) The logo.
Updates

Hi everyone, I am sorry for the delay. I have been out of town on unexpected business. I will make a decision this week. Thank you all for the great designs. Dale

```html
<!DOCTYPE html>
<html lang="en">
<head>
<meta charset="utf-8">
<title>Benefit Porter — Home</title>
<link href="https://fonts.googleapis.com/css2?family=Open+Sans:wght@400;600;700;800&family=Oswald:wght@400;500&display=swap" rel="stylesheet">
<style>
:root{
  --green:#5fb336;
  --green-dark:#4a9a26;
  --blue:#1d8cc8;
  --blue-dark:#156fa3;
  --teal:#17a39b;
  --ink:#333a40;
  --muted:#7b8389;
  --line:#e3e6e8;
  --page:#ffffff;
  --footer:#eef0f1;
}
*{box-sizing:border-box;margin:0;padding:0}
html,body{width:748px;height:1200px;overflow:hidden;background:var(--page)}
body{font-family:"Open Sans",Arial,sans-serif;color:var(--ink);font-size:7px;line-height:1.45;position:relative}
a{color:inherit;text-decoration:none}

.utility-bar{position:absolute;top:6px;right:20px;display:flex;gap:14px;font-size:6.5px;color:var(--muted)}
.utility-bar span::before{content:"";display:inline-block;width:5px;height:5px;background:var(--green);border-radius:50%;margin-right:3px;vertical-align:middle}

.masthead{position:absolute;top:22px;left:0;width:748px;height:40px;display:flex;align-items:center;justify-content:space-between;padding:0 20px 0 40px}
.brand{font-weight:600;font-size:14px;color:var(--ink);letter-spacing:.2px}
.main-nav{display:flex;font-size:6.5px;font-weight:600;letter-spacing:.3px}
.main-nav a{padding:14px 10px;color:var(--ink)}
.main-nav a.active{background:var(--green);color:#fff}

.hero{position:absolute;top:62px;left:0;width:748px;height:305px;background:linear-gradient(100deg,#eae7e2 0%,#d9d1c8 42%,#c9b7a7 62%,#b39a88 78%,#ddd5cc 100%)}
.hero-title{position:absolute;top:52px;left:40px;font-family:"Oswald","Arial Narrow",sans-serif;color:var(--teal);font-size:31px;line-height:1.08;font-weight:500;letter-spacing:.5px}
.hero-lead{position:absolute;top:125px;left:40px;width:210px;font-size:7px;color:var(--ink)}
.hero-list{position:absolute;top:152px;left:40px;list-style:none;font-size:6.5px}
.hero-list li{margin-bottom:4px}
.hero-list li::before{content:"";display:inline-block;width:4px;height:4px;background:var(--green);margin-right:5px;vertical-align:middle}
.btn{display:inline-block;background:var(--green);color:#fff;font-weight:700;font-size:9px;padding:7px 14px;letter-spacing:.5px}
.hero .btn{position:absolute;top:218px;left:40px;width:110px}

.feature-tiles{position:absolute;top:367px;left:40px;width:668px;height:50px;display:flex}
.tile{flex:1;color:#fff;padding:7px 10px;display:flex;gap:7px}
.tile-icon{width:18px;height:18px;border-radius:50%;border:2px solid #fff;flex:none}
.tile h3{font-size:9.5px;font-weight:700;letter-spacing:.4px}
.tile p{font-size:5.8px;line-height:1.35;opacity:.95}
.tile.green{background:var(--green)}.tile.blue{background:var(--blue)}.tile.teal{background:var(--teal)}.tile.blue-dark{background:var(--blue-dark)}

.intro-columns{position:absolute;top:438px;left:40px;width:668px;display:flex;gap:30px}
.intro-columns article{flex:1}
.intro-columns h2{font-size:10px;font-weight:700;margin-bottom:8px}
.intro-columns p{color:var(--muted);margin-bottom:10px}
.intro-columns em{color:var(--green);font-style:normal;font-weight:600}
.read-more{font-size:6px;font-weight:700;color:var(--ink)}
.read-more::after{content:" ›";color:var(--green)}

.testimonials{position:absolute;top:592px;left:0;width:748px;height:208px;background:var(--blue);color:#fff}
.section-head{display:flex;align-items:center;gap:8px;font-size:11px;font-weight:700}
.section-icon{width:20px;height:20px;border-radius:50%;background:#fff}
.testimonials .section-head{position:absolute;top:16px;left:40px}
.testimonials .section-icon{background:rgba(255,255,255,.9)}
.quote-row{position:absolute;top:48px;left:40px;width:668px;display:flex}
.quote{flex:1;text-align:center;padding:0 30px}
.avatar{width:66px;height:66px;border-radius:50%;border:3px solid #fff;margin:0 auto 8px;background:radial-gradient(circle at 50% 40%,#c9a590,#6d5448)}
.quote h4{font-size:8px;font-weight:700;margin-bottom:3px}
.quote p{font-size:6px;opacity:.9}

.events{position:absolute;top:812px;left:40px;width:668px}
.events .section-head{color:var(--ink);margin-bottom:12px}
.events .section-icon{background:var(--blue)}
.event-row{display:flex;gap:12px}
.event{flex:1}
.event-photo{height:88px;background:linear-gradient(160deg,#a9896a,#6b4e3c 55%,#3e3a44);margin-bottom:6px}
.event p{color:var(--muted);font-size:6px;margin-bottom:4px}

.site-footer{position:absolute;top:1018px;left:0;width:748px;height:182px;background:var(--footer);border-top:3px solid var(--green)}
.footer-cols{position:absolute;top:14px;left:40px;width:668px;display:flex;gap:24px}
.footer-cols section{flex:1}
.footer-cols h5{font-size:6.5px;font-weight:700;margin-bottom:7px;letter-spacing:.3px}
.footer-cols li{list-style:none;font-size:6px;color:var(--muted);margin-bottom:2px}
.social{display:flex;gap:5px;flex-wrap:wrap;width:60px}
.social i{width:18px;height:18px;background:#9aa2a8;display:block}
.footer-base{position:absolute;bottom:0;left:0;width:748px;height:26px;border-top:1px solid var(--line);display:flex;align-items:center;padding:0 40px;font-size:5.8px;color:var(--muted)}
</style>
</head>
<body>

<div class="utility-bar"><span>Sign In</span><span>Register</span><span>Sign Up for Email</span><span>Select a Language</span></div>

<header class="masthead">
  <div class="brand">Benefit Porter</div>
  <nav class="main-nav">
    <a class="active">HOME</a><a>PRICING</a><a>FEATURES</a><a>SERVICES</a><a>PRODUCTS</a><a>ABOUT</a><a>CONTACT</a>
  </nav>
</header>

<section class="hero" role="img" aria-label="Photo of a smiling woman forming a heart shape with her hands">
  <h1 class="hero-title">UT WISI ENIM AD<br>MINIM VENIAM</h1>
  <p class="hero-lead">Duis autem vel eum iriure dolor in hendrerit in vulputate velit esse molestie consequat, vel illum.</p>
  <ul class="hero-list">
    <li>Get Work Done in Fewer Steps Each Day</li>
    <li>Manage Every Event Online</li>
    <li>Grow Giving With Less Effort</li>
  </ul>
  <a class="btn">VIEW DETAIL</a>
</section>

<div class="feature-tiles">
  <div class="tile green"><span class="tile-icon"></span><div><h3>WELCOME</h3><p>Lorem ipsum dolor sit amet consectetur adipiscing elit sed diam nonummy.</p></div></div>
  <div class="tile blue"><span class="tile-icon"></span><div><h3>CHARITY</h3><p>Lorem ipsum dolor sit amet consectetur adipiscing elit sed diam nonummy.</p></div></div>
  <div class="tile teal"><span class="tile-icon"></span><div><h3>DONATE</h3><p>Lorem ipsum dolor sit amet consectetur adipiscing elit sed diam nonummy.</p></div></div>
  <div class="tile blue-dark"><span class="tile-icon"></span><div><h3>HELP</h3><p>Lorem ipsum dolor sit amet consectetur adipiscing elit sed diam nonummy.</p></div></div>
</div>

<div class="intro-columns">
  <article>
    <h2>Charity Success, Minus the Stress</h2>
    <p><em>Benefit Porter</em> can run your next benefit from the first invite to the final thank you. Plan, sell, track and report in one calm place built for busy teams and volunteers who need it easy.</p>
    <a class="read-more">READ MORE</a>
  </article>
  <article>
    <h2>Everything you Need</h2>
    <p>We <em>are experienced</em> in both the art of fundraising and the science behind it. Our tools help you <em>manage guests, tickets, sponsors and bids</em> with less effort and more giving every single season.</p>
    <a class="read-more">READ MORE</a>
  </article>
  <article>
    <h2>Solid Silent Auction Module</h2>
    <p>Everyone at <em>GivingDesk.com</em> loves our auction module. Bidders join from any phone, watch their items and get alerts when outbid, so your room stays lively and your totals keep <em>climbing</em>.</p>
    <a class="read-more">READ MORE</a>
  </article>
</div>

<section class="testimonials">
  <div class="section-head"><span class="section-icon"></span>Testimonials</div>
  <div class="quote-row">
    <div class="quote"><div class="avatar" role="img" aria-label="Portrait photo of Owen Harlow"></div><h4>Owen Harlow</h4><p>Lorem ipsum dolor sit amet, consectetuer adipiscing elit, sed diam nonummy nibh euismod tincidunt.</p></div>
    <div class="quote"><div class="avatar" role="img" aria-label="Portrait photo of Lena Marsh"></div><h4>Lena Marsh</h4><p>Lorem ipsum dolor sit amet, consectetuer adipiscing elit, sed diam nonummy nibh euismod tincidunt.</p></div>
    <div class="quote"><div class="avatar" role="img" aria-label="Portrait photo of Nora Quist"></div><h4>Nora Quist</h4><p>Lorem ipsum dolor sit amet, consectetuer adipiscing elit, sed diam nonummy nibh euismod tincidunt.</p></div>
  </div>
</section>

<section class="events">
  <div class="section-head"><span class="section-icon"></span>Seminars and Events</div>
  <div class="event-row">
    <div class="event"><div class="event-photo" role="img" aria-label="Photo of an audience at a seminar"></div><p>Lorem ipsum dolor sit amet, consectetur adipiscing elit sed diam nonummy nibh euismod.</p><a class="read-more">READ MORE</a></div>
    <div class="event"><div class="event-photo" role="img" aria-label="Photo of a speaker presenting to a group"></div><p>Lorem ipsum dolor sit amet, consectetur adipiscing elit sed diam nonummy nibh euismod.</p><a class="read-more">READ MORE</a></div>
    <div class="event"><div class="event-photo" role="img" aria-label="Photo of guests at a charity event"></div><p>Lorem ipsum dolor sit amet, consectetur adipiscing elit sed diam nonummy nibh euismod.</p><a class="read-more">READ MORE</a></div>
    <div class="event"><div class="event-photo" role="img" aria-label="Photo of a conference hall audience"></div><p>Lorem ipsum dolor sit amet, consectetur adipiscing elit sed diam nonummy nibh euismod.</p><a class="read-more">READ MORE</a></div>
  </div>
</section>

<footer class="site-footer">
  <div class="footer-cols">
    <section><h5>ABOUT THE COMMISSION</h5><ul><li>Our vision</li><li>Our partners</li><li>Our reports</li><li>Freedom of information</li><li>Operational guidance</li><li>Privacy policy</li></ul></section>
    <section><h5>OUR REGULATORY WORK</h5><ul><li>Secure charity number</li><li>Registering your event</li><li>New and older registration</li><li>Registration decisions</li><li>Approving changes to charities</li><li>How to complete a form</li></ul></section>
    <section><h5>DETAILED GUIDANCE</h5><ul><li>Registering a charity</li><li>Charitable purposes and public benefit</li><li>Trustees, staff and volunteers</li><li>Managing your charity</li><li>Money and accounts</li><li>Protecting your charity</li></ul></section>
    <section><h5>CONTACT US</h5><div class="social"><i></i><i></i><i></i><i></i></div></section>
  </div>
  <div class="footer-base"><span>© 2014 Benefit Porter. All rights reserved. Terms of use · Privacy</span></div>
</footer>

</body>
</html>
```